Harbor Winds Remember

The song is an instrumental song that was built around a slide show with an original poem, "Stand and Climb". I would like to do an Vextro digital booklet if possible.

The general vision for the album cover/possible Vextro digital booklet is a person coming from a dark place and just seeing a glimpse of light (representing hope of a better day).

Stills from the movie attached for reference.

Watch the movie on Flicksa .... http://flicksa.example/Q3mPzT7wKaL

```html
<!DOCTYPE html>
<html lang="en">
<head>
<meta charset="utf-8">
<title>Harbor Winds Remember – Booklet Cover Spread</title>
<link rel="stylesheet" href="https://fonts.googleapis.com/css2?family=Archivo+Black&family=Pathway+Gothic+One&display=swap">
<style>
  :root {
    --night: #000000;
    --ink: #050403;
    --gold: #e3b048;
    --gold-deep: #6b4712;
    --gold-dim: #4a3210;
    --amber: #c98a2a;
    --glow: #f6d79a;
    --paper: #ffffff;
    --spine-light: #8a6128;
    --spine-dark: #3c2610;
  }
  html, body {
    margin: 0;
    padding: 0;
    width: 1200px;
    height: 507px;
    overflow: hidden;
    background: var(--night);
  }
  .spread {
    display: block;
    width: 1200px;
    height: 507px;
  }
  .credit {
    font-family: "Pathway Gothic One", "Arial Narrow", sans-serif;
    font-size: 27px;
    fill: var(--paper);
    text-anchor: middle;
    letter-spacing: 0.5px;
  }
  .credit-mark {
    font-size: 14px;
  }
  .title-front {
    font-family: "Archivo Black", "Arial Black", sans-serif;
    font-size: 92px;
    fill: url(#title-fill);
  }
  .title-back {
    font-family: "Archivo Black", "Arial Black", sans-serif;
    font-size: 88px;
    fill: url(#title-back-fill);
  }
  .spine-title {
    font-family: "Pathway Gothic One", "Arial Narrow", sans-serif;
    font-size: 19px;
    fill: var(--gold);
    letter-spacing: 1px;
  }
</style>
</head>
<body>
<svg class="spread" viewBox="0 0 1200 507" xmlns="http://www.w3.org/2000/svg">
  <defs>
    <radialGradient id="front-glow" cx="870" cy="130" r="330" gradientUnits="userSpaceOnUse">
      <stop offset="0" stop-color="var(--glow)"/>
      <stop offset="0.25" stop-color="var(--amber)"/>
      <stop offset="0.6" stop-color="var(--gold-deep)" stop-opacity="0.7"/>
      <stop offset="1" stop-color="var(--night)" stop-opacity="0"/>
    </radialGradient>
    <radialGradient id="back-glow" cx="290" cy="230" r="300" gradientUnits="userSpaceOnUse">
      <stop offset="0" stop-color="var(--gold-dim)" stop-opacity="0.55"/>
      <stop offset="1" stop-color="var(--night)" stop-opacity="0"/>
    </radialGradient>
    <linearGradient id="figure-fill" x1="0" y1="0" x2="0" y2="1">
      <stop offset="0" stop-color="#2a1c0c"/>
      <stop offset="0.5" stop-color="#1a120a"/>
      <stop offset="1" stop-color="#5a4428"/>
    </linearGradient>
    <linearGradient id="title-fill" x1="0" y1="0" x2="0" y2="1">
      <stop offset="0" stop-color="var(--paper)"/>
      <stop offset="0.7" stop-color="#fbeed2"/>
      <stop offset="1" stop-color="#d9a654"/>
    </linearGradient>
    <linearGradient id="title-back-fill" x1="0" y1="0" x2="0" y2="1">
      <stop offset="0" stop-color="#5c4014"/>
      <stop offset="1" stop-color="#8a6124"/>
    </linearGradient>
    <linearGradient id="spine-fill" x1="0" y1="0" x2="1" y2="0">
      <stop offset="0" stop-color="var(--spine-dark)"/>
      <stop offset="0.5" stop-color="var(--spine-light)"/>
      <stop offset="1" stop-color="var(--spine-dark)"/>
    </linearGradient>
    <linearGradient id="skyline-fade" x1="0" y1="0" x2="0" y2="1">
      <stop offset="0" stop-color="var(--ink)" stop-opacity="0"/>
      <stop offset="0.45" stop-color="var(--ink)" stop-opacity="0.9"/>
      <stop offset="1" stop-color="var(--ink)"/>
    </linearGradient>
  </defs>

  <!-- Back cover -->
  <g class="back-cover">
    <rect x="0" y="0" width="574" height="507" fill="var(--night)"/>
    <rect x="0" y="0" width="574" height="507" fill="url(#back-glow)"/>
    <rect class="back-figure" x="195" y="20" width="110" height="420" rx="40" fill="#120c06" opacity="0.8" role="img" aria-label="Faint silhouette of the walking figure fading into the dark"/>
    <g class="back-title" opacity="0.85">
      <text class="title-back" x="32" y="283" textLength="520" lengthAdjust="spacingAndGlyphs">HARBOR</text>
      <text class="title-back" x="32" y="370" textLength="520" lengthAdjust="spacingAndGlyphs">WINDS</text>
      <text class="title-back" x="32" y="455" textLength="520" lengthAdjust="spacingAndGlyphs">REMEMBER</text>
    </g>
    <rect class="back-skyline" x="0" y="440" width="574" height="67" fill="url(#skyline-fade)" role="img" aria-label="City skyline silhouette along the bottom edge"/>
    <g class="back-credits">
      <text class="credit" x="250" y="139">“ STAND AND CLIMB<tspan class="credit-mark" dy="-2">©</tspan><tspan dy="2">”</tspan></text>
      <text class="credit" x="250" y="172">AN ORIGINAL POEM</text>
      <text class="credit" x="250" y="205">BY</text>
      <text class="credit" x="250" y="239">DALE CORVIN</text>
      <text class="credit" x="250" y="321">EDITORIAL SUPPORT</text>
      <text class="credit" x="250" y="354">BY</text>
      <text class="credit" x="250" y="388">INES HALLOWAY</text>
    </g>
  </g>

  <!-- Spine -->
  <g class="spine">
    <rect x="574" y="0" width="41" height="507" fill="url(#spine-fill)"/>
    <text class="spine-title" transform="translate(589 96) rotate(90)">HARBOR WINDS REMEMBER</text>
  </g>

  <!-- Front cover -->
  <g class="front-cover">
    <rect x="615" y="0" width="585" height="507" fill="var(--night)"/>
    <rect x="615" y="0" width="585" height="507" fill="url(#front-glow)"/>
    <rect class="front-figure" x="795" y="30" width="140" height="420" rx="30" fill="url(#figure-fill)" role="img" aria-label="Photograph of a long-haired figure in hat and coat walking out of the dark toward the light, carrying a bag and a guitar case"/>
    <g class="front-title">
      <text class="title-front" x="650" y="270" textLength="520" lengthAdjust="spacingAndGlyphs">HARBOR</text>
      <text class="title-front" x="650" y="372" textLength="520" lengthAdjust="spacingAndGlyphs">WINDS</text>
      <text class="title-front" x="636" y="465" textLength="538" lengthAdjust="spacingAndGlyphs">REMEMBER</text>
    </g>
    <rect class="front-skyline" x="615" y="455" width="585" height="52" fill="url(#skyline-fade)" role="img" aria-label="City skyline silhouette along the bottom edge"/>
  </g>
</svg>
</body>
</html>
```